Velmira - New coded website

Current website is around 5 years old and corrupted in some ways...
I would like to refresh the design and to create a new coded website based on the current content .
Please refer to :
www.velmira.com.au

Coding

Coded - Design and coding required

```html
<!DOCTYPE html>
<html lang="en">
<head>
<meta charset="utf-8">
<title>Contact Us | Velmira</title>
<link href="https://fonts.googleapis.com/css2?family=Poppins:wght@400;500;600;700;800&display=swap" rel="stylesheet">
<style>
:root{
  --green:#1f8f3a;
  --green-dark:#0f6a2b;
  --lime:#8cc63f;
  --navy:#0d4a6b;
  --ink:#111;
  --muted:#555;
  --line:#cfcfcf;
  --footer:#0b0b0b;
}
*{box-sizing:border-box;margin:0;padding:0}
html,body{width:1200px;height:2862px;overflow:hidden}
body{font-family:"Poppins",sans-serif;color:var(--ink);background:#fff;position:relative}
.abs{position:absolute}

/* header */
.site-header{position:absolute;top:0;left:0;width:1200px;height:96px;z-index:5}
.brand{position:absolute;left:123px;top:24px;display:flex;align-items:center;gap:10px;color:#fff;font-size:26px;font-weight:500;white-space:nowrap}
.brand .dot{width:44px;height:44px;border-radius:50%;background:var(--green)}
.main-nav{position:absolute;left:0;top:40px;width:1200px;height:16px;font-size:10px;color:#fff}
.main-nav span{position:absolute;top:0;white-space:nowrap}
.main-nav .active{color:var(--lime)}
.btn-quote{position:absolute;left:950px;top:32px;width:127px;height:32px;border-radius:16px;background:linear-gradient(90deg,var(--lime),var(--navy));color:#fff;font-size:10px;font-weight:700;display:flex;align-items:center;justify-content:center;white-space:nowrap}

/* hero */
.hero{position:absolute;top:0;left:0;width:1200px;height:590px}
.hero-photo{position:absolute;inset:0;background:linear-gradient(180deg,#2f5130 0%,#4f7b33 30%,#6c9a3a 55%,#3f6a2a 100%)}
.hero-title{position:absolute;top:282px;width:100%;text-align:center;color:#fff;font-size:40px;font-weight:800;letter-spacing:1px}
.hero-curve{position:absolute;left:0;top:470px}
.scroll-mouse{position:absolute;left:591px;top:486px;width:17px;height:28px;border:2px solid #555;border-radius:9px}
.scroll-mouse::after{content:"";position:absolute;left:5px;top:5px;width:3px;height:7px;background:#555;border-radius:2px}
.scroll-line{position:absolute;left:599px;top:526px;width:1px;height:62px;background:#bbb}

/* photo circles */
.ring-photo{position:absolute;border-radius:50%}
.ring-outer{border:1.5px solid var(--lime)}
.ring-mid{border:5px solid var(--green)}
.ring-img{border-radius:50%}

/* info */
.eyebrow{font-size:12.5px;font-weight:700;color:var(--green);letter-spacing:.5px}
.heading{font-size:33px;font-weight:800;letter-spacing:.5px;line-height:1.1;white-space:nowrap}
.intro{font-size:11px;color:var(--muted);line-height:1.75;width:340px}
.contact-item{display:flex;gap:10px;align-items:flex-start}
.contact-item .icon{width:30px;height:30px;border-radius:50%;background:var(--green);display:flex;align-items:center;justify-content:center;flex:none}
.contact-item .label{color:var(--green);font-size:12.5px;font-weight:500}
.contact-item .value{font-size:11.5px;line-height:1.3;margin-top:3px}

/* map */
.map{position:absolute;left:0;top:1177px;width:1200px;height:508px;background:linear-gradient(135deg,#eef0ec,#e6ebe4 60%,#dde7f0)}

/* form */
.field{position:absolute;border:1.5px solid #bdbdbd;border-radius:20px;font-size:11.5px;color:#666;padding:14px 16px}
.btn-submit{position:absolute;left:123px;top:2113px;width:130px;height:38px;border-radius:19px;background:linear-gradient(90deg,var(--lime),var(--navy));color:#fff;font-size:11.5px;font-weight:700;display:flex;align-items:center;justify-content:center}

/* newsletter */
.newsletter{position:absolute;left:0;top:2283px;width:1200px;height:370px;background:linear-gradient(90deg,#1c6a4a,#3a8a3a 60%,#4a9a3a)}
.skyline{position:absolute;left:0;bottom:0;width:1200px;height:150px;background:linear-gradient(180deg,rgba(13,74,80,0),rgba(13,74,80,.55))}
.news-input{position:absolute;left:345px;top:150px;width:510px;height:55px;background:#fff;border-radius:28px;font-size:12px;color:#666;padding:19px 18px}
.btn-subscribe{position:absolute;right:8px;top:8px;width:118px;height:39px;border-radius:20px;background:linear-gradient(90deg,var(--lime),var(--navy));color:#fff;font-size:11.5px;font-weight:700;display:flex;align-items:center;justify-content:center}

/* footer */
.site-footer{position:absolute;left:0;top:2653px;width:1200px;height:209px;background:var(--footer);color:#fff}
.footer-title{font-size:12.5px;font-weight:700}
.footer-title::after{content:"";display:block;width:55px;height:2px;background:var(--lime);margin-top:5px}
.footer-links{font-size:11px;line-height:22px;white-space:nowrap}
</style>
</head>
<body>

<header class="site-header">
  <div class="brand"><span class="dot"></span>Velmira</div>
  <nav class="main-nav">
    <span style="left:324px">Odour Control Products</span>
    <span style="left:458px">How Biofiltration Works</span>
    <span style="left:587px">Odour Control by Industry</span>
    <span style="left:732px">Past Projects</span>
    <span style="left:814px">About Us</span>
    <span class="active" style="left:878px">Contact</span>
  </nav>
  <div class="btn-quote">REQUEST A QUOTE</div>
</header>

<section class="hero">
  <div class="hero-photo" role="img" aria-label="Rolling green farmland hills at sunset"></div>
  <h1 class="hero-title">CONTACT US</h1>
  <svg class="hero-curve" width="1200" height="120" viewBox="0 0 1200 120">
    <path d="M0 10 Q600 180 1200 4 L1200 120 L0 120 Z" fill="#fff"/>
    <path d="M0 10 Q600 180 1200 4" fill="none" stroke="#0d4a6b" stroke-width="4"/>
  </svg>
  <div class="scroll-mouse"></div>
  <div class="scroll-line"></div>
</section>

<section class="contact-info">
  <div class="ring-photo ring-outer" style="left:128px;top:651px;width:444px;height:444px"></div>
  <div class="ring-photo ring-mid" style="left:145px;top:668px;width:410px;height:410px"></div>
  <div class="ring-img abs" role="img" aria-label="Hazy valley landscape with winding road" style="left:165px;top:688px;width:370px;height:370px;background:linear-gradient(180deg,#d8b98e,#8a8a5a 45%,#4a6a2a)"></div>

  <div class="abs" style="left:748px;top:733px">
    <div class="eyebrow">GET IN TOUCH</div>
    <h2 class="heading" style="margin-top:6px">CONTACT US</h2>
    <p class="intro" style="margin-top:12px">If you have any queries regarding out products, please do not hesitate to contact us</p>
    <div class="contact-item" style="margin-top:14px">
      <span class="icon"><svg width="14" height="14" viewBox="0 0 24 24"><path fill="#fff" d="M6.6 10.8a15 15 0 0 0 6.6 6.6l2.2-2.2a1 1 0 0 1 1-.25 11.4 11.4 0 0 0 3.6.6 1 1 0 0 1 1 1V20a1 1 0 0 1-1 1A17 17 0 0 1 3 4a1 1 0 0 1 1-1h3.5a1 1 0 0 1 1 1c0 1.250.2 2.45.6 3.6a1 1 0 0 1-.25 1z"/></svg></span>
      <div><div class="label">Call Us On</div><div class="value">+61 (08) 5550 2174</div></div>
    </div>
    <div class="contact-item" style="margin-top:20px">
      <span class="icon"><svg width="14" height="14" viewBox="0 0 24 24"><path fill="#fff" d="M12 2a7 7 0 0 0-7 7c0 5 7 13 7 13s7-8 7-13a7 7 0 0 0-7-7zm0 9.5A2.5 2.5 0 1 1 12 6.5a2.5 2.5 0 0 1 0 5z"/></svg></span>
      <div><div class="label">Our Location</div><div class="value">14 Harlow Crescent, Kingsmere WA 6071,<br>Australia</div></div>
    </div>
    <div class="contact-item" style="margin-top:18px;align-items:center">
      <span class="icon"></span>
      <div class="label">Follow Us</div>
    </div>
  </div>
</section>

<div class="map" role="img" aria-label="Street map showing the office location"></div>

<section class="contact-form">
  <div class="abs" style="left:123px;top:1803px">
    <div class="eyebrow">CONTACT US</div>
    <h2 class="heading" style="margin-top:6px">GET IN TOUCH</h2>
  </div>
  <div class="field" style="left:123px;top:1884px;width:205px;height:38px;padding:11px 16px">First Name</div>
  <div class="field" style="left:335px;top:1884px;width:205px;height:38px;padding:11px 16px">Last Name</div>
  <div class="field" style="left:123px;top:1935px;width:205px;height:38px;padding:11px 16px">Email</div>
  <div class="field" style="left:335px;top:1935px;width:205px;height:38px;padding:11px 16px">Phone</div>
  <div class="field" style="left:123px;top:1987px;width:418px;height:114px">Message</div>
  <div class="btn-submit">SUBMIT</div>

  <div class="ring-photo ring-outer" style="left:636px;top:1763px;width:444px;height:444px"></div>
  <div class="ring-photo ring-mid" style="left:653px;top:1780px;width:410px;height:410px"></div>
  <div class="ring-img abs" role="img" aria-label="Forested hills with wind turbines under a cloudy sky" style="left:673px;top:1800px;width:370px;height:370px;background:linear-gradient(180deg,#cfd9e2,#9fb0a0 35%,#8a8a3a 55%,#2f5a22)"></div>
</section>

<section class="newsletter">
  <div class="skyline" role="img" aria-label="City skyline silhouette"></div>
  <div class="abs" style="top:67px;width:100%;text-align:center">
    <div class="eyebrow" style="color:var(--lime)">KEEP UPTO DATE</div>
    <h2 class="heading" style="color:#fff;font-size:31px;margin-top:6px">SUBSCRIBE TO OUR NEWSLETTER</h2>
  </div>
  <div class="news-input">Enter Your Email<div class="btn-subscribe">SUBSCRIBE</div></div>
</section>

<footer class="site-footer">
  <div class="brand" style="left:177px;top:36px;font-size:40px"><span class="dot" style="width:62px;height:62px"></span>Velmira</div>
  <div class="abs" style="left:177px;top:129px;width:277px;height:1px;background:var(--green)"></div>
  <div class="abs" style="left:175px;top:150px;font-size:11px;white-space:nowrap">Copyright © 2010-2023 All rights reserved.</div>

  <div class="abs" style="left:567px;top:48px">
    <div class="footer-title">QUICK LINKS</div>
    <div class="footer-links" style="margin-top:10px">Odour Control Products<br>How Biofiltration Works<br>Odour Control by Industry</div>
  </div>
  <div class="footer-links abs" style="left:775px;top:78px">Past Projects<br>About Us</div>

  <div class="abs" style="left:930px;top:48px">
    <div class="footer-title">CONTACT US</div>
    <div class="footer-links" style="margin-top:8px;padding-left:27px;line-height:14px">
      <div style="margin-bottom:11px">+61 (08) 5550 2174</div>
      <div>14 Harlow Crescent,<br>Kingsmere WA 6071,<br>Australia</div>
    </div>
  </div>
</footer>

</body>
</html>
```